Letterhead, stationery and email signature for construction business

I need the letterhead, stationery and email signature designs for a construction business. I want them to have a corporate feel to them.

I've attached the logo for reference.

```html
<!DOCTYPE html>
<html lang="en">
<head>
<meta charset="utf-8">
<title>Harlow Builds – Business Card</title>
<link rel="stylesheet" href="https://fonts.googleapis.com/css2?family=Montserrat:wght@400;600;700;800&display=swap">
<style>
  :root {
    --brand-blue: #2a63b4;
    --brand-blue-light: #2f6fc2;
    --brand-blue-deep: #2557a6;
    --steel-grey: #4a4f63;
    --ink: #1d1f26;
    --paper: #ffffff;
    --backdrop: #e6e7ea;
  }
  * { box-sizing: border-box; margin: 0; padding: 0; }
  html, body {
    width: 1200px; height: 900px; overflow: hidden;
    background: var(--backdrop);
    font-family: "Montserrat", sans-serif;
  }
  .canvas {
    width: 1200px; height: 900px;
    display: flex; flex-direction: column; align-items: center; justify-content: center;
    gap: 36px;
  }
  .card {
    width: 700px; height: 400px; position: relative; overflow: hidden;
    box-shadow: 0 6px 18px rgba(0,0,0,.18);
  }

  /* Front */
  .card-front {
    background: radial-gradient(ellipse at 45% 30%, var(--brand-blue-light), var(--brand-blue-deep) 80%);
    display: flex; align-items: center; justify-content: center;
  }
  .wordmark {
    display: flex; align-items: center; gap: 16px;
    font-weight: 800; letter-spacing: 1px; text-transform: uppercase;
    white-space: nowrap;
  }
  .wordmark-square { width: 56px; height: 56px; flex: none; }
  .wordmark-text { font-size: 54px; line-height: 1; }
  .card-front .wordmark { color: var(--paper); }
  .card-front .wordmark-square { background: var(--paper); }

  /* Back */
  .card-back { background: var(--paper); }
  .card-back .swoosh { position: absolute; inset: 0; width: 100%; height: 100%; }
  .card-back .wordmark {
    position: absolute; left: 40px; top: 178px; gap: 12px; color: var(--brand-blue);
  }
  .card-back .wordmark-square { width: 34px; height: 34px; background: var(--brand-blue); }
  .card-back .wordmark-text { font-size: 27px; }
  .divider {
    position: absolute; left: 404px; top: 42px; width: 2px; height: 200px;
    background: var(--brand-blue);
  }
  .contact { position: absolute; left: 426px; top: 40px; color: var(--ink); }
  .contact-name { font-size: 22px; font-weight: 800; color: var(--brand-blue); letter-spacing: .3px; }
  .contact-role { font-size: 13px; font-weight: 400; margin: 4px 0 12px 4px; }
  .contact-address { font-size: 13px; font-weight: 700; line-height: 1.45; margin-bottom: 12px; margin-left: 4px; }
  .contact-list { list-style: none; font-size: 13px; font-weight: 700; margin-left: 4px; }
  .contact-list li { display: flex; align-items: center; gap: 8px; line-height: 1.7; }
  .icon { width: 14px; height: 14px; fill: var(--brand-blue); flex: none; }
</style>
</head>
<body>
<main class="canvas">
  <section class="card card-front" aria-label="Card front">
    <div class="wordmark">
      <span class="wordmark-square"></span>
      <span class="wordmark-text">Harlow Builds</span>
    </div>
  </section>

  <section class="card card-back" aria-label="Card back">
    <svg class="swoosh" viewBox="0 0 700 400" preserveAspectRatio="none" aria-hidden="true">
      <path d="M0 400 L0 374 C250 374 560 310 700 180 L700 400 Z" fill="var(--brand-blue)"/>
      <path d="M60 360 C300 354 560 290 672 200" fill="none" stroke="var(--steel-grey)" stroke-width="5" stroke-linecap="round"/>
    </svg>

    <div class="wordmark">
      <span class="wordmark-square"></span>
      <span class="wordmark-text">Harlow Builds</span>
    </div>

    <span class="divider"></span>

    <div class="contact">
      <h1 class="contact-name">DAN KESSLER</h1>
      <p class="contact-role">Co-Founder</p>
      <p class="contact-address">42-10 Birch Lane 8,<br>Ridgewood, NY 11206</p>
      <ul class="contact-list">
        <li><svg class="icon" viewBox="0 0 24 24"><path d="M6.6 10.8a15.1 15.1 0 0 0 6.6 6.6l2.2-2.2a1 1 0 0 1 1-.25 11.4 11.4 0 0 0 3.6.57 1 1 0 0 1 1 1V20a1 1 0 0 1-1 1A17 17 0 0 1 3 4a1 1 0 0 1 1-1h3.5a1 1 0 0 1 1 1c0 1.250.2 2.450.57 3.57a1 1 0 0 1-.25 1z"/></svg>555-214-7730</li>
        <li><svg class="icon" viewBox="0 0 24 24"><path d="M2 5h20v14H2z" fill="var(--brand-blue)"/><path d="M3 6l9 7 9-7" fill="none" stroke="#fff" stroke-width="1.6"/></svg>info@harlowbuilds.com</li>
        <li><svg class="icon" viewBox="0 0 24 24"><circle cx="12" cy="12" r="10"/></svg>www.harlowbuilds.com</li>
      </ul>
    </div>
  </section>
</main>
</body>
</html>
```